Southport Billboard for Hiring more CDL drivers

I need a catch design for a bill board (size 10ft by 36 ft) to catch the attention for semi truck drivers.
In the design I want it to include:
-My company logo along with my website(brisklanefreighters.com) and my number(503-217-6095) for contact info.
-I also need it to say earn up to $90,000 a year
-I will send a few photos to choose from
-I need the logo to look clean and simple! I don't want it to be cluttered just clean, simple and catchy.!

Target Market(s)

CDL Class A holders
Semi Truck Drivers

Industry/Entity Type

Trucking Company

Font styles to use
Other font styles liked:
• a font to match my logo

Requirements
Must have
• "Make up to $90,000"
"brisklanefreighters.com"
"503-217-6095"

```html
<!DOCTYPE html>
<html lang="en">
<head>
<meta charset="utf-8">
<title>Brisklane Freighters – Driver Hiring Billboard</title>
<link rel="stylesheet" href="https://fonts.googleapis.com/css2?family=Jost:wght@400;500;700;800&display=swap">
<style>
  :root {
    --panel-black: #16171b;
    --band-white: #f6f6f4;
    --ink: #17181c;
    --headline: #ffffff;
    --sky-top: #d4d8dd;
    --sky-mid: #a9b0b6;
    --truck-blue: #3f8fb0;
    --truck-red: #7a2a30;
    --asphalt: #4a4d52;
  }
  * { margin: 0; padding: 0; box-sizing: border-box; }
  html, body {
    width: 1200px;
    height: 333px;
    overflow: hidden;
    background: var(--panel-black);
  }
  .billboard {
    position: relative;
    width: 1200px;
    height: 333px;
    font-family: "Jost", sans-serif;
    background: var(--panel-black);
    overflow: hidden;
  }
  .truck-photo {
    position: absolute;
    left: 0;
    top: 0;
    width: 557px;
    height: 333px;
    background:
      linear-gradient(90deg, rgba(63,143,176,0.35) 0%, rgba(63,143,176,0.35) 48%, rgba(122,42,48,0.4) 52%, rgba(122,42,48,0.4) 100%),
      linear-gradient(180deg, var(--sky-top) 0%, var(--sky-mid) 40%, #8a8f95 70%, var(--asphalt) 100%);
  }
  .brand-name {
    position: absolute;
    left: 21px;
    top: 20px;
    font-weight: 800;
    font-size: 24px;
    letter-spacing: 0.5px;
    line-height: 1;
    color: var(--ink);
    text-transform: uppercase;
  }
  .headline {
    position: absolute;
    left: 557px;
    top: 45px;
    width: 643px;
    text-align: center;
    color: var(--headline);
    font-weight: 700;
    font-size: 70px;
    line-height: 63px;
    text-transform: uppercase;
  }
  .headline-line {
    display: block;
    white-space: nowrap;
  }
  .headline-line--first { letter-spacing: 0.5px; }
  .headline-line--second { letter-spacing: 1.5px; }
  .contact-band {
    position: absolute;
    left: 557px;
    top: 192px;
    width: 643px;
    height: 99px;
    background: var(--band-white);
    color: var(--ink);
    text-align: center;
    padding-top: 15px;
  }
  .contact-call {
    font-weight: 400;
    font-size: 43px;
    line-height: 42px;
    letter-spacing: -0.3px;
    white-space: nowrap;
  }
  .contact-call .phone { font-weight: 700; }
  .contact-web {
    font-weight: 400;
    font-size: 30px;
    line-height: 32px;
    letter-spacing: -0.3px;
    white-space: nowrap;
  }
  .contact-web .url { font-weight: 700; }
</style>
</head>
<body>
  <main class="billboard">
    <div class="truck-photo" role="img" aria-label="Photo of two semi trucks, a blue one and a red one, parked side by side under an overcast sky"></div>
    <div class="brand-name">Brisklane Freighters</div>

    <h1 class="headline">
      <span class="headline-line headline-line--first">Earn up to</span>
      <span class="headline-line headline-line--second">$90,000 a year</span>
    </h1>

    <section class="contact-band">
      <p class="contact-call">CALL US NOW <span class="phone">503-217-6095</span></p>
      <p class="contact-web">Or visit our website <span class="url">brisklanefreighters.com</span></p>
    </section>
  </main>
</body>
</html>
```